Tarjetas de visita para empresa de aluminio

Empresa con mas de 40 años vendiendo perfiles de aluminio.
Somos fábrica y almacén, queremos renovar la tarjeta de presentación de nuestros comerciales dando una imgen innovadora y tecnógica mezclado con la calidez del respeto al medio ambiente.
Añado el logo de la empresa y actual cara trasera de la tarjeta de visita, el logo es el simbolo WM y la marca TRAVENIC EXTRUSION, la frase 2extrusion y lacado de aluminio" debe cambiarse por "Diseño, extrusión, lacado, anodizado y mecanizado de precisión de aluminio" o en su defecto incluir todos esos servicios que hacemos o una frase mas pegadiza.

We are an aluminium factory, we produce and stock profiles of aluminium.
we want to renew visit card of our sellers, we are looking for something that show innovation, tecnology and environment respect.
Upload our actual logo and back of visit card, logo WM and brand TRAVENIC EXTRUSION must be keept.
Text "Extrusion y lacado de aluminio" must be changed for "Diseño, extrusion, lacado, anodizado y mecanizado de precisión de aluminio" or something like that

```html
<!DOCTYPE html>
<html lang="es">
<head>
<meta charset="utf-8">
<title>Tarjetas de visita – Travenic Extrusion</title>
<link rel="stylesheet" href="https://fonts.googleapis.com/css2?family=Lato:wght@400;700&family=Tinos&display=swap">
<style>
  :root {
    --stage: #999b9a;
    --card-light: #ffffff;
    --card-dark: #2b2b2c;
    --brand-blue: #1f4e86;
    --text-grey: #555a5e;
    --brand-steel: #3c3f43;
    --steel-light: #d9dadc;
    --steel-mid: #a9abae;
  }
  * { box-sizing: border-box; margin: 0; padding: 0; }
  html, body { width: 1200px; height: 1200px; overflow: hidden; }
  body { background: var(--stage); position: relative; font-family: "Lato", sans-serif; }

  .card { position: absolute; left: 222px; width: 755px; height: 463px; }
  .card--front { top: 105px; background: var(--card-light); }
  .card--back { top: 630px; background: var(--card-dark); }

  .brand { position: absolute; text-align: center; }
  .brand__mark { display: block; margin: 0 auto; border-radius: 50%; }
  .brand__name { font-family: "Lato", sans-serif; font-weight: 400; letter-spacing: 2px; white-space: nowrap; }
  .brand__tagline { font-family: "Lato", sans-serif; font-weight: 700; white-space: nowrap; }

  .card--front .brand { left: 40px; width: 370px; top: 52px; }
  .card--front .brand__mark { width: 140px; height: 86px; border: 3px solid var(--brand-steel); }
  .card--front .brand__name { margin-top: 14px; font-size: 27px; color: var(--brand-steel); }
  .card--front .brand__tagline { margin-top: 4px; font-size: 11px; line-height: 15px; letter-spacing: 1px; color: var(--brand-blue); }

  .person { position: absolute; left: 42px; top: 268px; }
  .person__name { font-family: "Tinos", serif; font-size: 29px; color: var(--brand-blue); white-space: nowrap; }
  .person__role { font-family: "Tinos", serif; font-size: 29px; color: var(--text-grey); margin-top: 2px; }
  .person__address { margin-top: 10px; font-size: 18px; line-height: 24px; color: var(--text-grey); }

  .contact { position: absolute; right: 44px; top: 283px; list-style: none; }
  .contact__item { display: flex; justify-content: flex-end; align-items: center; gap: 14px; height: 27px; font-size: 20px; color: var(--text-grey); }
  .contact__item--web { margin-top: 4px; }
  .contact__icon { width: 20px; height: 20px; fill: none; stroke: var(--brand-blue); stroke-width: 2; }

  .card--back .brand { left: 0; width: 755px; top: 126px; }
  .card--back .brand__mark { width: 216px; height: 134px; border: 4px solid var(--steel-light); }
  .card--back .brand__name { margin-top: 20px; font-size: 38px; color: var(--steel-light); letter-spacing: 4px; }
  .card--back .brand__tagline { margin-top: 8px; font-size: 16px; line-height: 22px; font-weight: 400; color: var(--steel-mid); letter-spacing: 3px; }
</style>
</head>
<body>
  <section class="card card--front">
    <div class="brand">
      <span class="brand__mark"></span>
      <p class="brand__name">TRAVENIC EXTRUSION</p>
      <p class="brand__tagline">DISEÑO, EXTRUSIÓN, LACADO, ANODIZADO<br>Y MECANIZADO DE PRECISIÓN DE ALUMINIO</p>
    </div>

    <div class="person">
      <p class="person__name">MARCOS OLIVERA PRIETO</p>
      <p class="person__role">Comercial</p>
      <p class="person__address">Pol. Ind. Almendros - C/4 Nº 12<br>45600 VILLALBA DEL CAMPO (Toledo)<br>Apartado de Correos 245</p>
    </div>

    <ul class="contact">
      <li class="contact__item">600 41 27 58
        <svg class="contact__icon" viewBox="0 0 20 20"><rect x="5" y="1" width="10" height="18" rx="2"/><line x1="9" y1="16" x2="11" y2="16"/></svg>
      </li>
      <li class="contact__item">900 52 14 73
        <svg class="contact__icon" viewBox="0 0 20 20"><path d="M2 8c0-3 3-4 8-4s8 1 8 4v1h-4V7H6v2H2z"/><rect x="4" y="10" width="12" height="8" rx="2"/><circle cx="10" cy="14" r="2"/></svg>
      </li>
      <li class="contact__item">900 52 14 73
        <svg class="contact__icon" viewBox="0 0 20 20"><rect x="5" y="2" width="10" height="5"/><rect x="2" y="7" width="16" height="7" rx="1"/><rect x="5" y="12" width="10" height="6"/></svg>
      </li>
      <li class="contact__item">marcosolivera@travenic.com
        <svg class="contact__icon" viewBox="0 0 20 20"><rect x="1" y="4" width="16" height="11"/><path d="M1 4l8 6 8-6"/></svg>
      </li>
      <li class="contact__item contact__item--web">www.travenic.com
        <svg class="contact__icon" viewBox="0 0 20 20"><circle cx="10" cy="10" r="8"/><ellipse cx="10" cy="10" rx="3.5" ry="8"/><line x1="2" y1="10" x2="18" y2="10"/><line x1="3.5" y1="6" x2="16.5" y2="6"/><line x1="3.5" y1="14" x2="16.5" y2="14"/></svg>
      </li>
    </ul>
  </section>

  <section class="card card--back">
    <div class="brand">
      <span class="brand__mark"></span>
      <p class="brand__name">TRAVENIC EXTRUSION</p>
      <p class="brand__tagline">DISEÑO, EXTRUSIÓN, LACADO, ANODIZADO<br>Y MECANIZADO DE PRECISIÓN DE ALUMINIO</p>
    </div>
  </section>
</body>
</html>
```